Marble Drakes - Sovereign rings, pendants & custom cultural pieces

I need a website that attracts customers knowing that I am as per detailed below Everyone deserves a special piece of treasure. At Marble Drakes we provide you with unique, high-quality and affordable Sovereign rings, pendants & custom cultural pieces.
Feel free to check my Instagram page to get idea's @marble.drakes
I want people to see the Items I have available & know that my prices are very competitive. I want people to be able to Shop/Purchase items via site. I would like to have Marble Drakes Facebook, Instagram & Bidloft Icon/tabs on site so customers can link a at click of the mouse.

(My Apologies to you all, This is all overwhelming & new to myself & I appreciate your efforts & work detail)
Updates

Apologies, have had family loss to deal with

Still dealing with loss of family member

Still Dealing with Family member passing

As previously, still getting through the loss of a family member

As per previous extensions, re adjusting to life after loss of family member

As per previously still recovering from loss of family member

As previously expressed

Haven’t recovered from family loss

I am still getting life back together

Target Market(s)

Jewellery, Wedding, Gifts, Pacific people, Persons 18 - 65yrs, New Zealand & Australian

Industry/Entity Type

Jewelry

Contact Information for Business Card

Marble Drakes
Reto Amusel
Facebook @marbledrakes
Instagram @marble.drakes
Phone Number 021 04731952
Website www.marbledrakes.co.nz
Auckland
New Zealand

Number of Pages Required

5+ page

Font styles to use
Sans Serif

Colors
474747
1b1b1b
000000
cfcfcf
fbed22
ffc214
ffffff

Requirements
Must have
• Using Black / Gold Marble Drakes logo with crown, has been attached to Web design.
• Reto Amusel
• Facebook Marble Drakes
• Instagram @marble.drakes
• Bidloft Marble Drakes
• Phone Number 021 04731952
• Website www.marbledrakes.co.nz
Nice to have
• Thinking black card with the Marble Drakes Gold logo
• Lines on back of card for Customer Quoted Prices

```html
<!DOCTYPE html>
<html lang="en">
<head>
<meta charset="utf-8">
<title>Marble Drakes – Business Card Front</title>
<link rel="stylesheet" href="https://fonts.googleapis.com/css2?family=Cinzel:wght@500&display=swap">
<style>
  :root {
    --card-black: #000000;
    --antique-gold: #7f6d1f;
    --pure-white: #ffffff;
    --soft-grey: #cfcfcf;
  }
  html, body {
    margin: 0;
    padding: 0;
    width: 1200px;
    height: 685px;
    overflow: hidden;
    background: var(--card-black);
  }
  .business-card {
    position: relative;
    width: 1200px;
    height: 685px;
    background: var(--card-black);
    overflow: hidden;
  }
  .accent-bar {
    position: absolute;
    border-radius: 8px;
  }
  .accent-bar--white-top { left: 148px; top: -10px; width: 13px; height: 290px; background: var(--pure-white); }
  .accent-bar--gold-top { left: 192px; top: -10px; width: 17px; height: 405px; background: var(--antique-gold); }
  .accent-bar--gold-bottom { left: 991px; top: 305px; width: 17px; height: 400px; background: var(--antique-gold); }
  .accent-bar--white-bottom { left: 1039px; top: 400px; width: 13px; height: 300px; background: var(--pure-white); }

  .brand-lockup {
    position: absolute;
    left: 0;
    right: 0;
    top: 170px;
    display: flex;
    flex-direction: column;
    align-items: center;
  }
  .brand-mark {
    width: 190px;
    height: 190px;
    border-radius: 50%;
    background: var(--antique-gold);
  }
  .brand-name {
    margin: 52px 0 0;
    font-family: "Cinzel", serif;
    font-weight: 500;
    font-size: 44px;
    letter-spacing: 1px;
    color: var(--pure-white);
    line-height: 1;
  }
  .brand-rule {
    margin-top: 22px;
    width: 400px;
    display: flex;
    justify-content: space-between;
  }
  .brand-rule span {
    display: block;
    width: 104px;
    height: 3px;
    background: var(--soft-grey);
  }
</style>
</head>
<body>
  <main class="business-card">
    <div class="accent-bar accent-bar--white-top"></div>
    <div class="accent-bar accent-bar--gold-top"></div>
    <div class="accent-bar accent-bar--gold-bottom"></div>
    <div class="accent-bar accent-bar--white-bottom"></div>

    <div class="brand-lockup">
      <div class="brand-mark"></div>
      <h1 class="brand-name">Marble Drakes</h1>
      <div class="brand-rule"><span></span><span></span></div>
    </div>
  </main>
</body>
</html>
```